SkyvoraQ Business Cards and Stationary Design

Need a design for our business cards and stationary. I want to carry on the theme of the logo. I want the business cards to have a design on the back. I would like the business cards and the stationary to carry the same theme, design scheme, and branding

Target Market(s)

Airlines and Maintenance Facilities

Industry/Entity Type

Aviation

Contact Information for Business Card

Name
Position Title
Address: 4827 Tollbeck Lane, Fort Pierce, Florida, 34951
Office Number
Mobile Number
Email
Website

Font styles to use
Serif
Sans Serif

Colors

Designer to choose colors to be used in the design.

```html
<!DOCTYPE html>
<html lang="en">
<head>
<meta charset="utf-8">
<title>SkyvoraQ Business Card</title>
<link href="https://fonts.googleapis.com/css2?family=Open+Sans:wght@300;400;700&display=swap" rel="stylesheet">
<style>
  :root {
    --backdrop-light: #3ea8e5;
    --backdrop-mid: #1f4fae;
    --backdrop-deep: #0a1670;
    --card-black: #0e0f12;
    --band-light: #45c0f1;
    --band-mid: #2a6fcf;
    --band-deep: #071f8c;
    --text-white: #ffffff;
    --icon-disc: #e9edf2;
    --icon-glyph: #1a1d24;
  }
  * { margin: 0; padding: 0; box-sizing: border-box; }
  html, body { width: 1200px; height: 1200px; overflow: hidden; }
  body {
    position: relative;
    font-family: "Open Sans", Arial, sans-serif;
    color: var(--text-white);
    background: linear-gradient(160deg, var(--backdrop-light) 0%, var(--backdrop-mid) 50%, var(--backdrop-deep) 100%);
  }
  .card {
    position: absolute;
    width: 710px;
    height: 419px;
    background: var(--card-black);
    box-shadow: 0 18px 40px rgba(0, 0, 0, 0.45);
    overflow: hidden;
  }
  .card-front { left: 246px; top: 124px; }
  .card-back { left: 245px; top: 639px; }

  .band {
    position: absolute;
    right: 0;
    background: linear-gradient(150deg, var(--band-light) 0%, var(--band-mid) 45%, var(--band-deep) 100%);
    box-shadow: -6px 10px 14px rgba(0, 0, 0, 0.55);
  }
  .card-front .band {
    left: 134px; top: 81px; height: 257px;
    border-radius: 128px 0 0 128px;
  }
  .card-back .band {
    left: 289px; top: 54px; height: 307px; right: 2px;
    border-radius: 180px 0 0 180px / 153px 0 0 153px;
  }

  .wordmark {
    position: absolute;
    left: 0; right: 0; top: 50%;
    transform: translateY(-50%);
    text-align: center;
    font-weight: 700;
    font-size: 46px;
    letter-spacing: 0.16em;
    padding-left: 0.16em;
  }

  .identity {
    position: absolute;
    left: 0; width: 272px; top: 176px;
    text-align: right;
  }
  .identity-name {
    font-size: 33px;
    line-height: 40px;
    font-weight: 300;
    letter-spacing: 0.01em;
  }
  .identity-name strong { font-weight: 400; }
  .identity-role {
    font-size: 21px;
    font-weight: 300;
    line-height: 28px;
    margin-top: -2px;
  }

  .contact-list { list-style: none; }
  .contact-item {
    position: absolute;
    left: 78px;
    display: flex;
    align-items: center;
    gap: 12px;
    font-size: 21px;
    font-weight: 400;
    line-height: 22px;
    transform: translateY(-50%);
  }
  .contact-icon {
    flex: none;
    width: 30px; height: 30px;
    border-radius: 50%;
    background: var(--icon-disc);
    display: flex; align-items: center; justify-content: center;
  }
  .contact-icon svg { width: 16px; height: 16px; stroke: var(--icon-glyph); fill: none; stroke-width: 1.6; stroke-linecap: round; stroke-linejoin: round; }
  .contact-item.office { top: 60px; }
  .contact-item.email { top: 107px; }
  .contact-item.mobile { top: 157px; }
  .contact-item.address { top: 206px; }
  .contact-item.address .contact-text { padding-left: 4px; }
  .contact-item.web { top: 253px; }
</style>
</head>
<body>
  <section class="card card-front" aria-label="Business card front">
    <div class="band">
      <div class="wordmark">SKYVORAQ</div>
    </div>
  </section>

  <section class="card card-back" aria-label="Business card back">
    <div class="identity">
      <p class="identity-name">DANA <strong>WHITFIELD</strong></p>
      <p class="identity-role">Director</p>
    </div>
    <div class="band">
      <ul class="contact-list">
        <li class="contact-item office">
          <span class="contact-icon"><svg viewBox="0 0 16 16"><rect x="2" y="2" width="4" height="12" rx="1"/><rect x="7" y="3" width="7" height="11" rx="1"/><path d="M9 5h3M9 8h1M11 8h1M9 11h1M11 11h1"/></svg></span>
          <span class="contact-text">(255) 318 4406</span>
        </li>
        <li class="contact-item email">
          <span class="contact-icon"><svg viewBox="0 0 16 16"><rect x="2" y="4" width="12" height="9" rx="1"/><path d="M2.5 4.5 8 9l5.5-4.5"/></svg></span>
          <span class="contact-text">dwhitfield@skyvoraq.com</span>
        </li>
        <li class="contact-item mobile">
          <span class="contact-icon"><svg viewBox="0 0 16 16"><rect x="5" y="2" width="6" height="12" rx="1"/><path d="M3 6v4M1.5 7v2M13 6v4M14.5 7v2"/></svg></span>
          <span class="contact-text">124 706 3318</span>
        </li>
        <li class="contact-item address">
          <span class="contact-icon"><svg viewBox="0 0 16 16"><path d="M8 14.5s-4-4.3-4-7.5a4 4 0 0 1 8 0c0 3.2-4 7.5-4 7.5z" fill="var(--icon-glyph)"/><circle cx="8" cy="7" r="1.4" fill="var(--icon-disc)" stroke="none"/></svg></span>
          <span class="contact-text">4827 Tollbeck Lane,<br>Fort Pierce, Florida, 34951</span>
        </li>
        <li class="contact-item web">
          <span class="contact-icon"><svg viewBox="0 0 16 16"><circle cx="8" cy="8" r="6"/><ellipse cx="8" cy="8" rx="2.6" ry="6"/><path d="M2 8h12M3 5h10M3 11h10"/></svg></span>
          <span class="contact-text">Skyvoraq.com</span>
        </li>
      </ul>
    </div>
  </section>
</body>
</html>
```